Atelier Marrow Architecture business card

We need to update our business card. We do high end custom residential, hospitality, and wellness architecture. We focus on creating unique spaces and design around the five senses, believing that architecture's true impact is not on our surroundings, but within us. We would like to see designs are instill a sense of calm awe. They should be crisp, fresh, clean, authentic, & contemporary without being sterile, overworked, or harsh. White space is important. Alternative materials are an option if natural. We have created our own logo and would like designs to incorporate it. However, we are willing to see alternatives if the logo becomes a stumbling block and you have an alternate you suggest. Card must have the following information:
Atelier Marrow Architecture, Inc.
728 Holloway Ct. NE Atlanta, GA 30318
Marcus T. Whitcombe, AIA, NCARB, LEED AP BD+C
ateliermarrow.example

Target Market(s)

Higher net worth individuals with an appreciation for design, nature, sustainability,

Industry/Entity Type

Architect

Contact Information for Business Card

See above. The title of Owner or Architect is helpful but not necessary. Minimalism should trump additional information.

Font styles to use
Serif
Sans Serif

Requirements
Must have
• It should look professional. It must use logo
Should not have
• caligraphy, animals, anything that is cute,

```html
<!DOCTYPE html>
<html lang="en">
<head>
<meta charset="utf-8">
<title>Atelier Marrow Architecture — Business Card</title>
<link rel="stylesheet" href="https://fonts.googleapis.com/css2?family=Tenor+Sans&display=swap">
<style>
  :root {
    --page: #e9e9e7;
    --card: #f7f7f5;
    --ink: #1f1f1f;
    --ink-soft: #3a3a3a;
    --brand-green: #2e8536;
    --card-shadow: rgba(0, 0, 0, 0.12);
  }
  * { box-sizing: border-box; margin: 0; padding: 0; }
  html, body {
    width: 1200px;
    height: 861px;
    overflow: hidden;
    background: var(--page);
    font-family: "Tenor Sans", sans-serif;
    color: var(--ink);
  }
  .canvas {
    position: relative;
    width: 1200px;
    height: 861px;
    display: flex;
    flex-direction: column;
    align-items: center;
    justify-content: center;
    gap: 40px;
  }
  .card {
    position: relative;
    width: 660px;
    height: 377px;
    background: var(--card);
    box-shadow: 0 2px 10px var(--card-shadow);
  }
  .card-front .wordmark {
    position: absolute;
    top: 44px;
    left: 250px;
    font-size: 20px;
    letter-spacing: 0.22em;
    text-transform: uppercase;
    color: var(--ink);
    line-height: 1.4;
  }
  .card-front .wordmark .wordmark-sub {
    display: block;
    font-size: 10px;
    letter-spacing: 0.78em;
  }
  .identity {
    position: absolute;
    top: 128px;
    left: 70px;
  }
  .identity .person-name {
    font-size: 19px;
    letter-spacing: 0.04em;
    margin-bottom: 4px;
  }
  .identity .credentials,
  .identity .role {
    font-size: 13.5px;
    color: var(--ink-soft);
    letter-spacing: 0.03em;
    line-height: 1.45;
  }
  .contact {
    position: absolute;
    top: 222px;
    left: 70px;
    list-style: none;
    font-size: 13.5px;
    line-height: 1.6;
    letter-spacing: 0.03em;
    color: var(--ink-soft);
  }
  .address {
    position: absolute;
    right: 48px;
    bottom: 44px;
    font-style: normal;
    font-size: 15px;
    line-height: 1.5;
    letter-spacing: 0.05em;
  }
  .card-back .brand-mark {
    position: absolute;
    left: 160px;
    top: 150px;
  }
</style>
</head>
<body>
  <main class="canvas">
    <section class="card card-front">
      <div class="wordmark">Atelier Marrow<span class="wordmark-sub">Architecture</span></div>
      <div class="identity">
        <p class="person-name">Marcus T. Whitcombe</p>
        <p class="credentials">AIA, NCARB, LEED AP BD+C</p>
        <p class="role">Owner</p>
      </div>
      <ul class="contact">
        <li>404.555.0162</li>
        <li>info@ateliermarrow.example</li>
        <li>ateliermarrow.example</li>
      </ul>
      <address class="address">728 Holloway Ct. NE<br>Atlanta, GA 30318</address>
    </section>

    <section class="card card-back">
      <svg class="brand-mark" width="300" height="130" viewBox="0 0 300 130" role="img" aria-label="Green brush-stroke mark">
        <rect x="0" y="0" width="300" height="130" rx="40" fill="var(--brand-green)"/>
      </svg>
    </section>
  </main>
</body>
</html>
```